Marbrook Jewelers New Website Design

This project is to provide a new design for an existing website. The existing website is marbrookjewelers dot com . I have created a overview document that outlines all the details for the project. I do not need the design to be converted into HTML. I have a team for that already so please don't ask. I have a lot of images .. too many to upload here so they are on my dev server located at pinfernstudio com slash marbrook slash assets

Number of Pages Required

1 page

```html
<!DOCTYPE html>
<html lang="en">
<head>
<meta charset="utf-8">
<title>Marbrook Jewelers</title>
<link rel="stylesheet" href="https://fonts.googleapis.com/css2?family=Poppins:wght@400;500;600&display=swap">
<style>
:root{
  --teal:#6aa9ae;
  --aqua:#99dce0;
  --pale:#eef5f6;
  --grey:#f2f2f2;
  --ink:#111111;
  --text:#555555;
  --white:#ffffff;
  --photo-dark:#0e0f18;
}
*{box-sizing:border-box;margin:0;padding:0}
html,body{width:1200px;height:3686px;overflow:hidden}
body{position:relative;font-family:'Poppins',sans-serif;color:var(--ink);background:var(--white)}
.abs{position:absolute}
.photo{position:absolute}
.btn{position:absolute;background:var(--teal);color:var(--white);border-radius:20px;font-size:14px;display:flex;align-items:center;justify-content:center}
.section-title{position:absolute;left:0;width:1200px;text-align:center;font-size:26px;font-weight:500;letter-spacing:.5px}
.icon-ring{width:38px;height:38px;flex:none;border:1.5px solid #3d4b4f;border-radius:50%;display:flex;align-items:center;justify-content:center}
.contact{position:absolute;display:flex;align-items:center;gap:14px;font-size:13px;color:#444;line-height:19px}
.contact.strong{font-weight:500;color:#222;font-size:14px}

/* header */
.nav-band{top:59px;left:0;width:1200px;height:38px;background:var(--teal)}
.nav-link{position:absolute;top:68px;color:var(--white);font-size:14px}
.logo-badge{top:12px;left:543px;width:114px;height:114px;border-radius:50%;background:var(--white);border:3px solid var(--teal);display:flex;align-items:center;justify-content:center;font-size:17px;color:#3d4b4f;text-align:center;line-height:20px}

/* hero */
.hero-right{top:97px;left:644px;width:556px;height:540px;background:var(--pale)}
.hero-brand{top:245px;left:684px;font-size:18px;color:var(--teal)}
.hero-title{top:278px;left:684px;font-size:41px;line-height:52px;font-weight:500}
.hero-text{top:388px;left:684px;width:460px;font-size:13.5px;line-height:22px;color:var(--text)}
.slide-dot{position:absolute;left:1154px;width:30px;height:30px;border:1.5px solid #333;border-radius:50%;font-size:11px;display:flex;align-items:center;justify-content:center}

/* products */
.product-circle{position:absolute;top:778px;width:252px;height:252px;border-radius:50%;border:4px solid var(--teal)}
.product-label{position:absolute;top:1038px;width:252px;text-align:center;font-size:19px;color:var(--teal)}
.arrow-btn{position:absolute;top:886px;width:34px;height:34px;border-radius:50%;display:flex;align-items:center;justify-content:center}

/* about */
.about-band{top:1146px;left:0;width:1200px;height:423px;background:var(--grey)}
.about-title{top:1204px;left:673px;font-size:26px;font-weight:500}
.about-text{top:1251px;left:673px;width:462px;font-size:13.5px;line-height:22.5px;color:var(--text)}

/* service cards */
.card{position:absolute;top:1653px;width:339px;height:250px;background:#000;overflow:hidden}
.card-wedge{position:absolute;right:0;top:0;width:170px;height:250px;border-radius:250px 0 0 250px/125px 0 0 125px}
.card-title{position:absolute;top:40px;left:20px;font-size:18px;font-weight:500;color:var(--teal)}
.card-text{position:absolute;top:74px;left:20px;width:145px;font-size:13px;line-height:22.5px;color:var(--white)}

/* gallery */
.gallery-band{top:1988px;left:0;width:1200px;height:796px;background:var(--aqua)}
.view-more{position:absolute;top:2693px;left:548px;width:104px;height:37px;border-radius:20px;background:var(--white);font-size:14px;display:flex;align-items:center;justify-content:center}

/* footer */
.footer{top:3265px;left:0;width:1200px;height:379px;background:var(--teal)}
.footer-logo{top:3298px;left:526px;width:148px;height:148px;border-radius:50%;background:var(--white);border:3px solid #e6f2f3;display:flex;align-items:center;justify-content:center;font-size:21px;color:#3d4b4f}
.footer-link{position:absolute;top:3474px;color:var(--white);font-size:14px}
.footer-contact{color:var(--white)!important}
.footer-contact .icon-ring{background:var(--white);border-color:var(--white)}
.social{position:absolute;top:3582px;width:36px;height:36px;border-radius:50%;background:var(--white);display:flex;align-items:center;justify-content:center}
.copyright{top:3644px;left:0;width:1200px;height:42px;background:var(--ink);color:var(--white);font-size:11.5px;display:flex;align-items:center;justify-content:center}
</style>
</head>
<body>

<!-- header -->
<div class="contact" style="top:10px;left:58px">
  <span class="icon-ring"><svg width="18" height="18" viewBox="0 0 24 24" fill="none" stroke="#3d4b4f" stroke-width="1.8"><path d="M12 22s7-7 7-12a7 7 0 0 0-14 0c0 5 7 12 7 12z"/><circle cx="12" cy="10" r="2.5"/></svg></span>
  <span>48 Alder Ave N, Brookfield,<br>MN</span>
</div>
<div class="contact" style="top:10px;left:299px">
  <span class="icon-ring"><svg width="18" height="18" viewBox="0 0 24 24" fill="none" stroke="#3d4b4f" stroke-width="1.8"><rect x="3" y="6" width="18" height="13" rx="1"/><path d="M3 7l9 7 9-7"/></svg></span>
  <span>info@marbrookjewelers.com</span>
</div>
<div class="contact strong" style="top:10px;left:735px">
  <span class="icon-ring"><svg width="18" height="18" viewBox="0 0 24 24" fill="none" stroke="#3d4b4f" stroke-width="1.8"><path d="M5 3h4l2 5-3 2a11 11 0 0 0 6 6l2-3 5 2v4a2 2 0 0 1-2 2A17 17 0 0 1 3 5a2 2 0 0 1 2-2z"/></svg></span>
  <span>612-555-0148</span>
</div>
<div class="contact" style="top:10px;left:914px">
  <span class="icon-ring"><svg width="18" height="18" viewBox="0 0 24 24" fill="none" stroke="#3d4b4f" stroke-width="1.8"><circle cx="12" cy="12" r="9"/><path d="M12 7v5l3 2"/></svg></span>
  <span>Mon-Sat: 10:Am To :Pm<br>Sun: &nbsp;Closed</span>
</div>

<div class="abs nav-band"></div>
<span class="nav-link" style="left:61px">Company</span>
<span class="nav-link" style="left:155px">Custom Jewelery</span>
<span class="nav-link" style="left:298px">Jewelery Repair</span>
<span class="nav-link" style="left:431px">Resources</span>
<span class="nav-link" style="left:682px">Show Case</span>
<span class="nav-link" style="left:783px">Gallery</span>
<span class="nav-link" style="left:854px">Engraving &amp; Trophies</span>
<span class="nav-link" style="left:1024px">Gift Ideas</span>
<svg class="abs" style="top:68px;left:1120px" width="20" height="20" viewBox="0 0 24 24" fill="none" stroke="#fff" stroke-width="2"><circle cx="10" cy="10" r="7"/><path d="M15 15l6 6"/></svg>
<div class="abs logo-badge">Marbrook<br>Jewelers</div>

<!-- hero -->
<div class="photo" role="img" aria-label="Amethyst pear ring with silver band on dark background" style="top:97px;left:0;width:644px;height:540px;background:radial-gradient(ellipse 150px 130px at 50% 42%,#a63fd0 0%,#6c3a8c 35%,rgba(80,70,100,.6) 60%,transparent 100%),radial-gradient(ellipse 230px 200px at 50% 45%,#6d6874 0%,#2a2536 55%,var(--photo-dark) 100%)"></div>
<div class="abs hero-right"></div>
<div class="abs hero-brand">Marbrook Jewelers</div>
<div class="abs hero-title">NEW COLLECTION<br>2022</div>
<div class="abs hero-text">Lorem Ipsum is simply dummy text of the printing and typesetting industry.</div>
<div class="btn" style="top:465px;left:684px;width:104px;height:37px">Shop Now</div>
<div class="slide-dot" style="top:307px">01</div>
<div class="slide-dot" style="top:352px">02</div>
<div class="slide-dot" style="top:398px">03</div>
<div class="photo" role="img" aria-label="Loose blue and white gemstones" style="top:528px;left:1050px;width:150px;height:76px;border-radius:50%;background:linear-gradient(120deg,#1e3f5e,#9ab0bd 60%,#dfe6ea)"></div>

<!-- products -->
<div class="section-title" style="top:713px">OUR PRODUCTS</div>
<div class="arrow-btn" style="left:14px;background:var(--teal)"><svg width="14" height="14" viewBox="0 0 24 24" fill="none" stroke="#fff" stroke-width="2.5"><path d="M15 5l-7 7 7 7"/></svg></div>
<div class="arrow-btn" style="left:1153px;border:1.5px solid #333"><svg width="14" height="14" viewBox="0 0 24 24" fill="none" stroke="#333" stroke-width="2.5"><path d="M9 5l7 7-7 7"/></svg></div>
<div class="product-circle" role="img" aria-label="Pair of silver wedding bands" style="left:63px;background:radial-gradient(ellipse 90px 55px at 50% 50%,#d9d9dc 0%,#8c8c90 45%,#1a1a1a 80%,#000 100%)"></div>
<div class="product-circle" role="img" aria-label="Diamond huggie earrings" style="left:336px;background:radial-gradient(ellipse 95px 65px at 50% 50%,#e2e2e4 0%,#909094 45%,#1a1a1a 80%,#000 100%)"></div>
<div class="product-circle" role="img" aria-label="Steel wristwatch with white dial" style="left:610px;background:radial-gradient(ellipse 60px 120px at 50% 50%,#ecebf0 0%,#a7a4ad 40%,#2a2a2e 78%,#000 100%)"></div>
<div class="product-circle" role="img" aria-label="Diamond bangle bracelet" style="left:888px;background:radial-gradient(ellipse 100px 75px at 50% 50%,#000 0%,#2a2022 40%,#d8c8ca 62%,#6a6062 75%,#000 95%)"></div>
<span class="product-label" style="left:63px">Ring</span>
<span class="product-label" style="left:336px">Earrings</span>
<span class="product-label" style="left:610px">Watch</span>
<span class="product-label" style="left:888px">Bracelets</span>

<!-- about -->
<div class="abs about-band"></div>
<div class="photo" role="img" aria-label="Blue gemstone" style="top:1156px;left:0;width:80px;height:70px;border-radius:50%;background:linear-gradient(135deg,#3a6a90,#0f2336)"></div>
<div class="photo" role="img" aria-label="Hand wearing a diamond ring" style="top:1198px;left:60px;width:419px;height:258px;border-radius:8px;background:linear-gradient(120deg,#3a3430,#c9a999 45%,#e4cfc4 60%,#5a4c46)"></div>
<div class="photo" role="img" aria-label="Video still of rings on dark wood" style="top:1263px;left:355px;width:242px;height:242px;border-radius:50%;border:4px solid var(--teal);background:radial-gradient(circle at 50% 40%,#8a7f78,#4a3a30 45%,#1d1a18)"></div>
<div class="abs" style="top:1367px;left:458px;width:34px;height:34px;border-radius:50%;background:var(--teal);display:flex;align-items:center;justify-content:center"><svg width="12" height="12" viewBox="0 0 12 12"><path d="M3 1l8 5-8 5z" fill="#fff"/></svg></div>
<div class="abs about-title">ABOUT US</div>
<p class="abs about-text">Marbrook Jewelers is an independent, family owned jewelry store located in the heart of Downtown Brookfield. Owner, Daniel Marbrook has been with the business since 1990. His wife, Helen, joined the business in 2010, store manager, Tom, came on board in 2016 and Lucia joined the team in 2021. Marbrook Jewelers specializes in engagement rings, fashion jewelry and custom designed pieces. Whether you want to create the ring of your dreams or re-create a family heirloom, Marbrook Jewelers is the place to go.</p>
<div class="btn" style="top:1466px;left:665px;width:107px;height:36px">Read More</div>

<!-- service cards -->
<div class="card" style="left:60px">
  <div class="card-wedge" role="img" aria-label="Silver ring with blue diamond" style="background:radial-gradient(ellipse 70px 50px at 45% 45%,#e6e6e8 0%,#7a7a80 40%,#8fbcc3 75%)"></div>
  <div class="card-title">Jewelery Repair</div>
  <p class="card-text">Lorem Ipsum is simply dummy text of the printing and typesetting industry.</p>
  <div class="btn" style="top:186px;left:20px;width:104px;height:36px">Shop Now</div>
</div>
<div class="card" style="left:429px">
  <div class="card-wedge" role="img" aria-label="Engraved gold cross pendant" style="background:radial-gradient(ellipse 45px 95px at 55% 50%,#b58a5c 0%,#8a5a34 45%,#93d3d8 75%)"></div>
  <div class="card-title">Gift Ideas</div>
  <p class="card-text">Lorem Ipsum is simply dummy text of the printing and typesetting industry.</p>
  <div class="btn" style="top:186px;left:20px;width:104px;height:36px">Shop Now</div>
</div>
<div class="card" style="left:799px">
  <div class="card-wedge" role="img" aria-label="Assorted blue sapphires" style="background:radial-gradient(ellipse 55px 90px at 50% 50%,#2a4a8a 0%,#3a5a90 40%,#8fbcc3 75%)"></div>
  <div class="card-title">Resources</div>
  <p class="card-text">Lorem Ipsum is simply dummy text of the printing and typesetting industry.</p>
  <div class="btn" style="top:186px;left:20px;width:104px;height:36px">Shop Now</div>
</div>

<!-- gallery -->
<div class="abs gallery-band"></div>
<div class="section-title" style="top:2045px">OUR GALLERY</div>
<div class="photo" role="img" aria-label="Diamond tennis bracelet on black" style="top:2109px;left:60px;width:532px;height:301px;background:radial-gradient(ellipse 260px 70px at 50% 72%,#8a8a8a 0%,#3a3a3a 45%,transparent 80%),radial-gradient(ellipse at 50% 40%,#1e1e1e,#050505)"></div>
<div class="btn" style="top:2241px;left:274px;width:119px;height:37px">Add To Cart</div>
<div class="photo" role="img" aria-label="Oval sapphire ring in gift box" style="top:2109px;left:606px;width:262px;height:226px;background:radial-gradient(ellipse 40px 35px at 52% 45%,#1c2f8a 0%,#3a4a90 40%,transparent 70%),linear-gradient(135deg,#e0c8bf,#b59a90)"></div>
<div class="photo" role="img" aria-label="Ruby and diamond pendant necklace" style="top:2109px;left:878px;width:262px;height:226px;background:radial-gradient(ellipse 30px 40px at 50% 55%,#b01a4a 0%,#d07a90 40%,#e9e4e6 70%,#ffffff 100%)"></div>
<div class="photo" role="img" aria-label="Stacked diamond rings on a hand" style="top:2423px;left:60px;width:260px;height:224px;background:radial-gradient(ellipse 55px 65px at 50% 40%,#f2f2f4 0%,#d8c2b4 50%,transparent 80%),linear-gradient(135deg,#c98f78,#8e5a4a)"></div>
<div class="photo" role="img" aria-label="Blue dial diver watch" style="top:2423px;left:332px;width:260px;height:224px;background:radial-gradient(circle at 45% 55%,#1f3468 0%,#2a3f78 32%,#c9c9cf 45%,#f2f2f4 60%,#ffffff 100%)"></div>
<div class="photo" role="img" aria-label="Tahitian pearl ring on black" style="top:2347px;left:606px;width:534px;height:300px;background:radial-gradient(circle 60px at 50% 45%,#9fb0aa 0%,#4a5a55 60%,transparent 100%),radial-gradient(ellipse 150px 120px at 50% 45%,#4a4a42,#040404)"></div>
<a class="view-more">View More</a>
<div class="photo" role="img" aria-label="Loose white diamond" style="top:2728px;left:1108px;width:90px;height:56px;border-radius:50%;background:linear-gradient(135deg,#f4f6f7,#a9b1b5)"></div>

<!-- social feed -->
<div class="section-title" style="top:2872px">WE ARE ON &nbsp;PAGEWALL</div>
<div class="photo" role="img" aria-label="Solitaire ring on black" style="top:2930px;left:60px;width:262px;height:250px;background:radial-gradient(ellipse 60px 35px at 50% 50%,#c9c9d2 0%,#5a5a66 45%,#15151c 80%,#08080c 100%)"></div>
<div class="photo" role="img" aria-label="Pearl ring on black" style="top:2930px;left:333px;width:262px;height:250px;background:radial-gradient(ellipse 45px 45px at 50% 45%,#a9b8b2 0%,#4e5c57 50%,#0c0c0c 85%,#050505 100%)"></div>
<div class="photo" role="img" aria-label="Diamond bracelet on black" style="top:2930px;left:606px;width:262px;height:250px;background:radial-gradient(ellipse 120px 40px at 50% 52%,#c8c2a8 0%,#5a5648 45%,#111 80%,#050505 100%)"></div>
<div class="photo" role="img" aria-label="Amethyst ring on black" style="top:2930px;left:878px;width:262px;height:250px;background:radial-gradient(ellipse 50px 45px at 50% 50%,#b44ad8 0%,#6a3a8a 45%,#1a1424 80%,#080810 100%)"></div>

<!-- footer -->
<div class="abs footer"></div>
<div class="abs footer-logo">Marbrook</div>
<span class="footer-link" style="left:165px">Company</span>
<span class="footer-link" style="left:258px">Custom Jewelery</span>
<span class="footer-link" style="left:401px">Jewelery Repair</span>
<span class="footer-link" style="left:535px">Resources</span>
<span class="footer-link" style="left:630px">Show Case</span>
<span class="footer-link" style="left:730px">Gallery</span>
<span class="footer-link" style="left:802px">Engraving &amp; Trophies</span>
<span class="footer-link" style="left:972px">Gift Ideas</span>

<div class="contact footer-contact" style="top:3515px;left:160px">
  <span class="icon-ring"><svg width="18" height="18" viewBox="0 0 24 24" fill="none" stroke="#3d4b4f" stroke-width="1.8"><path d="M12 22s7-7 7-12a7 7 0 0 0-14 0c0 5 7 12 7 12z"/><circle cx="12" cy="10" r="2.5"/></svg></span>
  <span>48 Alder Ave N, Brookfield,<br>MN</span>
</div>
<div class="contact footer-contact" style="top:3515px;left:400px">
  <span class="icon-ring"><svg width="18" height="18" viewBox="0 0 24 24" fill="none" stroke="#3d4b4f" stroke-width="1.8"><rect x="3" y="6" width="18" height="13" rx="1"/><path d="M3 7l9 7 9-7"/></svg></span>
  <span>info@marbrookjewelers.com</span>
</div>
<div class="contact strong footer-contact" style="top:3515px;left:648px">
  <span class="icon-ring"><svg width="18" height="18" viewBox="0 0 24 24" fill="none" stroke="#3d4b4f" stroke-width="1.8"><path d="M5 3h4l2 5-3 2a11 11 0 0 0 6 6l2-3 5 2v4a2 2 0 0 1-2 2A17 17 0 0 1 3 5a2 2 0 0 1 2-2z"/></svg></span>
  <span>612-555-0148</span>
</div>
<div class="contact footer-contact" style="top:3515px;left:828px">
  <span class="icon-ring"><svg width="18" height="18" viewBox="0 0 24 24" fill="none" stroke="#3d4b4f" stroke-width="1.8"><circle cx="12" cy="12" r="9"/><path d="M12 7v5l3 2"/></svg></span>
  <span>Mon-Sat: 10:Am To :Pm<br>Sun: &nbsp;Closed</span>
</div>
<a class="social" style="left:554px" aria-label="Pagewall"><svg width="16" height="16" viewBox="0 0 24 24" fill="none" stroke="#222" stroke-width="2"><circle cx="18" cy="5" r="2.5"/><circle cx="6" cy="12" r="2.5"/><circle cx="18" cy="19" r="2.5"/><path d="M8.2 10.8l7.6-4.5M8.2 13.2l7.6 4.5"/></svg></a>
<a class="social" style="left:609px" aria-label="Pinboardly"><svg width="16" height="16" viewBox="0 0 24 24" fill="none" stroke="#222" stroke-width="2"><path d="M10 14a4 4 0 0 0 6 0l3-3a4 4 0 0 0-6-6l-1 1"/><path d="M14 10a4 4 0 0 0-6 0l-3 3a4 4 0 0 0 6 6l1-1"/></svg></a>

<div class="abs copyright">© 2022 &nbsp;MARBROOK JEWELERS. All rights reserved</div>
</body>
</html>
```